International Food Manufacturer in the need of a new business card and logo.

Our Company - Brightfield Provisions Ltd.

Our Industry - Food and Drink

We are a Wild Harvested Food Distributor / Manufacturer. We service the following food sectors: Supermarkets, Hotels, Restaurants, Cafes, Catering and all people looking to eat healthy food products.

Slogan - The foremost source for everything healthy

Business card details -

48-52 Quarrow Lane
Ashby Meadow
London
NP7 3RD United Kingdom
Morven Tillick
+44 7700 900412 - UK
+971 50 5550137 - UAE
+38 067 555 0198 - Ukraine
morven@brightfieldprovisions.com
www.brightfieldprovisions.com

Goal - We are looking for a dynamic modern new look for our corporate image and a designer who can bring this new concept to our future food product designs. Please try to incorporate 3d hexagonal vector Imaging in your design concepts.

Target Market(s)

Industry/Entity Type

Food Service

Contact Information for Business Card

Brightfield Provisions Ltd.
48-52 Quarrow Lane
Ashby Meadow
London
NP7 3RD United Kingdom
Morven Tillick
+44 7700 900412 - UK
+971 50 5550137 - UAE

Font styles to use
Serif

Colors

Designer to choose colors to be used in the design.

Requirements
Must have
• Please read project description above.
Nice to have
Should not have

```html
<!DOCTYPE html>
<html lang="en">
<head>
<meta charset="utf-8">
<title>Brightfield Provisions – Business Card</title>
<link rel="stylesheet" href="https://fonts.googleapis.com/css2?family=Libre+Baskerville&family=Roboto:wght@400;500&display=swap">
<style>
  :root {
    --page-bg: #e9ebe8;
    --leaf-green: #4b6b1d;
    --leaf-green-light: #5a7d26;
    --leaf-green-dark: #3d5a15;
    --ink: #111111;
    --paper: #ffffff;
    --pattern-grey: #eef0ed;
    --serif: "Libre Baskerville", Georgia, serif;
    --sans: "Roboto", Arial, sans-serif;
  }
  html, body {
    margin: 0;
    width: 1200px;
    height: 798px;
    overflow: hidden;
    background: var(--page-bg);
  }
  .canvas {
    position: relative;
    width: 1200px;
    height: 798px;
  }
  .card {
    position: absolute;
    width: 520px;
    height: 300px;
    border-radius: 16px;
    overflow: hidden;
    box-shadow: 0 8px 24px rgba(0,0,0,0.18);
  }
  .card-front {
    left: 110px;
    top: 80px;
    background: var(--leaf-green);
  }
  .card-back {
    left: 570px;
    top: 400px;
    background: var(--paper);
  }
  .pattern-fill {
    position: absolute;
    inset: 0;
    width: 100%;
    height: 100%;
  }
  .brand-name {
    font-family: var(--serif);
    font-weight: 400;
    font-size: 24px;
    color: var(--ink);
    margin: 0;
    white-space: nowrap;
  }
  .front-lockup {
    position: absolute;
    right: 44px;
    top: 136px;
  }
  .back-lockup {
    position: absolute;
    left: 34px;
    top: 54px;
    display: flex;
    align-items: center;
    gap: 10px;
  }
  .brand-dot {
    width: 12px;
    height: 12px;
    border-radius: 50%;
    background: var(--leaf-green);
  }
  .back-pattern {
    position: absolute;
    right: 0;
    top: 50px;
    width: 190px;
    height: 170px;
  }
  .person {
    position: absolute;
    left: 34px;
    top: 186px;
    font-family: var(--sans);
    color: var(--ink);
  }
  .person-name {
    font-size: 15px;
    font-weight: 500;
    margin: 0;
    text-transform: uppercase;
  }
  .person-role {
    font-size: 10px;
    font-weight: 500;
    margin: 2px 0 14px;
  }
  .address {
    font-style: normal;
    font-size: 10px;
    line-height: 1.45;
  }
  .contact-rule {
    position: absolute;
    left: 262px;
    top: 150px;
    width: 3px;
    height: 100px;
    background: var(--leaf-green);
  }
  .contacts {
    position: absolute;
    left: 276px;
    top: 150px;
    margin: 0;
    padding: 0;
    list-style: none;
    font-family: var(--sans);
    font-size: 10.5px;
    line-height: 1.55;
    color: var(--ink);
  }
</style>
</head>
<body>
<main class="canvas">

  <section class="card card-front" aria-label="Business card front">
    <svg class="pattern-fill" viewBox="0 0 520 300" role="img" aria-label="Repeating four-petal leaf pattern in darker greens">
      <defs>
        <linearGradient id="frontPattern" x1="0" y1="0" x2="1" y2="1">
          <stop offset="0" stop-color="#5a7d26"/>
          <stop offset="0.55" stop-color="#4b6b1d"/>
          <stop offset="1" stop-color="#3d5a15"/>
        </linearGradient>
      </defs>
      <rect width="520" height="300" fill="url(#frontPattern)"/>
    </svg>
    <div class="front-lockup">
      <p class="brand-name">Brightfield Provisions</p>
    </div>
  </section>

  <section class="card card-back" aria-label="Business card back">
    <svg class="back-pattern" viewBox="0 0 190 170" role="img" aria-label="Faint leaf pattern in light grey">
      <defs>
        <radialGradient id="backPattern" cx="0.6" cy="0.5" r="0.6">
          <stop offset="0" stop-color="#eef0ed"/>
          <stop offset="1" stop-color="#ffffff"/>
        </radialGradient>
      </defs>
      <rect width="190" height="170" fill="url(#backPattern)"/>
    </svg>

    <div class="back-lockup">
      <p class="brand-name">Brightfield Provisions</p>
      <span class="brand-dot" aria-hidden="true"></span>
    </div>

    <div class="person">
      <p class="person-name">Morven Tillick</p>
      <p class="person-role">President &amp; CEO</p>
      <address class="address">
        48-52 Quarrow Lane<br>
        Ashby Meadow, London<br>
        NP7 3RD United Kingdom
      </address>
    </div>

    <div class="contact-rule" aria-hidden="true"></div>
    <ul class="contacts">
      <li>+44 7700 900412 - UK</li>
      <li>+971 50 5550137 - UAE</li>
      <li>+38 067 555 0198 - Ukraine</li>
      <li>morven@brightfieldprovisions.com</li>
      <li>www.brightfieldprovisions.com</li>
    </ul>
  </section>

</main>
</body>
</html>
```